Tor Ridge Wine Club-The Onyx Roll

We are a new aspirational brand of fine Tasmania Wine. We need a commitment club poster which appeals to the ego.We have one opportunity to get customers to sign up and that is when they visit at the cellar door. This club is the core of our business.

The brand is a clean, pure , simple brand, black and white very sophiscated.
This is a top end product.

Our Commitment Club is named The Onyx Roll which is a play on words. Tradionally The Onyx Roll is a list of people that you dont want to do business with. So we are turning this on its had.

You need to make this poster sharp, desirable, possibly sexy but masculine. Im thinking Felix Crane . It doesnt matter the client will be 40 up fashion consious looking for something new , exclusive , something there peers don't have.

I dont like busy! make it clean clear and basically undeniable. The client must not be able to resist the offer.

www.torridgevines.com.au

Reason: Internet problems so cant get to respond and offer comment in a timely manner

Appreciator 40-60 male wants to be recognised fashion consious sophiscated has money and wants to part of something exclusive.

A feeling that you are part of something that only a few are. Exclusive

Maybe an imagine of beautiful people 30/40ish I want to be drinking Tor Wine / in The Onyx Roll

Fashion

Must have
• Tor Ridge Logo
TOR Bottles images

We produce only 1600 cases of wine each vintage. Therefore we have limited membership 001-999 for our club.
Award Winning Wines available exclusively from us.

Gold Member
We will reserve 2 cases of our limited vintage, to be delivered to you in May and Oct.
Single varietal or mixed cases. You receive a 15% discount.

Silver Member
We will reserve 1 case of our limited vintage to be delivered to you 6 bottles in May and 6 in Oct.
Single varietal or mixed cases. You receive a 10% discount.

To you exclusively from us not, available from any other retailers.

You will be invited to Onyx Roll Only Events and Tastings.
You will get preferential access to new and limited releases.
Members will be entered in a bi annual draw to win a 2 night stay here at the Tor Weavers Cottage on the Freycinet Coast Tasmania.

• VIP stamps,gimacs, anything that cheapens our brand.

We do not like busy posters please have white space

```html
<!DOCTYPE html>
<html lang="en">
<head>
<meta charset="utf-8">
<title>Join The Onyx Roll — Tor Ridge</title>
<link rel="stylesheet" href="https://fonts.googleapis.com/css2?family=Cinzel:wght@400;600;700&family=Great+Vibes&family=Montserrat:ital,wght@1,800&display=swap">
<style>
  :root {
    --ink: #000000;
    --paper: #ffffff;
    --gold-light: #fff3a8;
    --gold-mid: #e8b92a;
    --gold-deep: #a86e08;
    --gold-text: #d9a520;
    --silver: #e6e6e6;
    --logo-ink: #1c0a12;
    --glow: rgba(255, 255, 255, 0.07);
  }
  * { margin: 0; padding: 0; box-sizing: border-box; }
  html, body {
    width: 1200px;
    height: 900px;
    overflow: hidden;
    background: var(--ink);
  }
  .poster {
    position: relative;
    width: 1200px;
    height: 900px;
    background: var(--ink);
    overflow: hidden;
  }
  .backdrop {
    position: absolute;
    inset: 0;
    background: radial-gradient(circle at 990px 593px, var(--glow) 0%, rgba(255, 255, 255, 0.03) 45%, var(--ink) 80%);
  }
  .gold-fill {
    background: linear-gradient(180deg, var(--gold-light) 0%, var(--gold-mid) 45%, var(--gold-deep) 75%, var(--gold-mid) 100%);
    -webkit-background-clip: text;
    background-clip: text;
    color: transparent;
  }
  .headline {
    position: absolute;
    left: 56px;
    top: 322px;
    width: 678px;
    text-align: right;
    font-family: "Cinzel", serif;
    font-weight: 700;
    font-size: 72px;
    line-height: 60px;
    letter-spacing: 14px;
  }
  .headline-rule {
    position: absolute;
    left: 62px;
    top: 455px;
    width: 660px;
    height: 2px;
    background: linear-gradient(90deg, var(--gold-deep), var(--gold-light), var(--gold-mid));
  }
  .levels {
    position: absolute;
    left: 140px;
    top: 494px;
    display: flex;
    align-items: center;
    gap: 22px;
  }
  .levels-number {
    font-family: "Montserrat", sans-serif;
    font-style: italic;
    font-weight: 800;
    font-size: 72px;
    line-height: 1;
  }
  .levels-label {
    font-family: "Cinzel", serif;
    font-weight: 700;
    font-size: 29px;
    line-height: 28px;
    letter-spacing: 7px;
  }
  .tier {
    position: absolute;
    top: 590px;
    font-family: "Cinzel", serif;
  }
  .tier-gold { left: 40px; color: var(--gold-text); }
  .tier-silver { left: 414px; color: var(--silver); }
  .tier-name {
    font-family: "Great Vibes", cursive;
    font-size: 46px;
    line-height: 46px;
    font-weight: 400;
    margin-bottom: 6px;
  }
  .tier-terms {
    font-size: 11.5px;
    line-height: 23px;
    letter-spacing: 0.3px;
  }
  .tier-gold .tier-terms { padding-left: 20px; }
  .tier-gold .tier-terms span { display: block; }
  .tier-gold .tier-terms span + span { padding-left: 8px; }
  .benefits {
    position: absolute;
    left: 90px;
    top: 746px;
    width: 600px;
    list-style: none;
    text-align: center;
    font-family: "Cinzel", serif;
    font-size: 12.5px;
    line-height: 29px;
    letter-spacing: 0.4px;
    color: var(--paper);
  }
  .brand-disc {
    position: absolute;
    left: 808px;
    top: 411px;
    width: 364px;
    height: 364px;
    border-radius: 50%;
    background: var(--paper);
    display: flex;
    align-items: center;
    justify-content: center;
  }
  .brand-name {
    font-family: "Cinzel", serif;
    font-weight: 600;
    font-size: 40px;
    letter-spacing: 2px;
    color: var(--logo-ink);
  }
</style>
</head>
<body>
<main class="poster">
  <div class="backdrop" role="img" aria-label="Fine silver spiral lines sweeping out from the brand disc across the black background"></div>

  <h1 class="headline gold-fill">JOIN THE<br>ONYX ROLL</h1>
  <div class="headline-rule"></div>

  <div class="levels">
    <span class="levels-number gold-fill">002</span>
    <span class="levels-label gold-fill">LEVELS OF<br>COMMITMENT</span>
  </div>

  <section class="tier tier-gold">
    <h2 class="tier-name">Gold Membership</h2>
    <p class="tier-terms">
      <span>Reserve 2 cases of Wine delivered to you</span>
      <span>1 May 1 Oct You choose the variety 15% discount</span>
    </p>
  </section>

  <section class="tier tier-silver">
    <h2 class="tier-name">Silver Membership</h2>
    <p class="tier-terms">
      Reserve 1/2 case of your choice of wine delivered<br>
      to you 1 May 1 Oct you choose your variety 10% discount
    </p>
  </section>

  <ul class="benefits">
    <li>Not available with other retailers Exclusively to you from us.</li>
    <li>Preferential access to first releases and limited releases</li>
    <li>VIP access to Onyx Roll only tastings and events.</li>
  </ul>

  <div class="brand-disc">
    <span class="brand-name">Tor Ridge</span>
  </div>
</main>
</body>
</html>
```